Banner Ad Design

Need design of small banners for page margins on a Printing website that is currently under development. Need designs for these 4 promo items:

Table Tents (1000): $217
Flyers (5000): $328
Postcards (5000): $237
Brochures (5000): $386

Use the same detail text that is shown in the attached examples - such as "Full Color Front 14 pt, etc, etc". Pricing and quantity should be as provided above.

Color scheme and images should also be similar to what is shown. Banner sizes should be 120 x 120.

```html
<!DOCTYPE html>
<html lang="en">
<head>
<meta charset="utf-8">
<title>Print Specials Banners</title>
<link rel="stylesheet" href="https://fonts.googleapis.com/css2?family=Arimo:wght@400;700&family=Open+Sans:wght@700;800&display=swap">
<style>
  :root {
    --page-bg: #ffffff;
    --card-top: #ffffff;
    --card-bottom: #e4e4e4;
    --card-border: #c9c9c9;
    --detail-text: #555555;
    --qty-text: #7a7a7a;
    --orange: #ee7418;
    --pink: #e8176a;
    --sky: #2a8be0;
    --violet: #c21fdc;
    --title-blue: #1a73c4;
    --title-red: #d8191f;
    --title-purple: #8a1496;
    --green-hi: #a6d35a;
    --green-lo: #6fa832;
    --blue-hi: #2b93ea;
    --blue-lo: #0a56b0;
    --red-hi: #f04a46;
    --red-lo: #b8141a;
    --cyan-hi: #5ff0ec;
    --cyan-lo: #16b8b8;
    --photo-warm: #e79a5c;
    --photo-dark: #2a2a2a;
  }
  * { margin: 0; padding: 0; box-sizing: border-box; }
  html, body { width: 1200px; height: 900px; overflow: hidden; background: var(--page-bg); }
  .canvas { position: relative; width: 1200px; height: 900px; }

  .promo {
    position: absolute;
    width: 120px; height: 116px;
    border: 1px solid var(--card-border);
    border-radius: 10px;
    background: linear-gradient(to bottom, var(--card-top) 30%, var(--card-bottom));
    overflow: hidden;
    font-family: "Arimo", Arial, sans-serif;
    box-shadow: 0 1px 2px rgba(0,0,0,.12);
  }
  .ribbon {
    position: absolute;
    left: -34px; top: 8px;
    width: 100px; height: 17px;
    transform: rotate(-45deg);
    color: #fff;
    font-size: 10px; font-weight: 700;
    text-align: center; line-height: 17px;
  }
  .product-photo {
    position: absolute;
    right: 4px; top: 3px;
    width: 78px; height: 40px;
    border-radius: 2px;
    background: linear-gradient(120deg, var(--photo-dark) 0 28%, #f3f3f3 28% 34%, var(--photo-warm) 34% 70%, #cfcfcf 70%);
  }
  .product-photo.tall { width: 46px; right: 20px; height: 48px; top: 0; }
  .product-photo.brochure { width: 62px; height: 42px; right: 6px; background: linear-gradient(160deg, #d9b48f 0 50%, var(--photo-dark) 50%); }
  .product-photo.postcard { background: linear-gradient(120deg, #fff 0 30%, var(--photo-warm) 30% 72%, #cfcfcf 72%); border: 1px solid #444; }

  .detail {
    position: absolute;
    left: 5px; top: 48px;
    font-size: 9px; line-height: 10px;
    color: var(--detail-text);
  }
  .detail.brochure-detail { top: 46px; }
  .title {
    position: absolute;
    left: 4px; top: 68px;
    font-size: 16px; font-weight: 700;
    letter-spacing: -0.3px;
  }
  .title.brochure-title { top: 65px; }
  .qty {
    position: absolute;
    left: 4px; top: 92px;
    color: var(--qty-text);
    font-size: 15px; font-weight: 700;
  }
  .qty small { font-size: 8px; font-weight: 400; margin-left: 2px; }
  .price {
    position: absolute;
    left: 55px; top: 82px;
    width: 60px; height: 36px;
    border-radius: 50%;
    border: 2px solid rgba(255,255,255,.9);
    color: #fff;
    font-family: "Open Sans", Arial, sans-serif;
    font-weight: 800; font-size: 17px;
    text-align: center; line-height: 32px;
    text-shadow: 0 1px 1px rgba(0,0,0,.35);
  }

  .v-orange .ribbon { background: var(--orange); }
  .v-orange .title { color: var(--orange); }
  .v-orange .price { background: radial-gradient(ellipse at 50% 20%, var(--green-hi), var(--green-lo)); }
  .v-pink .ribbon { background: var(--pink); }
  .v-pink .title { color: var(--title-blue); }
  .v-pink .price { background: radial-gradient(ellipse at 50% 20%, var(--blue-hi), var(--blue-lo)); }
  .v-sky .ribbon { background: var(--sky); }
  .v-sky .title { color: var(--title-red); }
  .v-sky .price { background: radial-gradient(ellipse at 50% 20%, var(--red-hi), var(--red-lo)); }
  .v-violet .ribbon { background: var(--violet); }
  .v-violet .title { color: var(--title-purple); }
  .v-violet .price { background: radial-gradient(ellipse at 50% 20%, var(--cyan-hi), var(--cyan-lo)); }

  .col-1 { left: 264px; } .col-2 { left: 444px; } .col-3 { left: 624px; } .col-4 { left: 804px; }
  .row-1 { top: 77px; } .row-2 { top: 274px; } .row-3 { top: 461px; } .row-4 { top: 658px; }
</style>
</head>
<body>
<main class="canvas">
  <!-- Flyers -->
  <div class="promo v-orange col-1 row-1"><div class="product-photo" role="img" aria-label="Stack of printed flyers"></div><div class="ribbon">Special</div><p class="detail">Full Color Front<br>100 lb Gloss + AQ</p><h2 class="title">Flyers</h2><p class="qty">5000<small>for</small></p><p class="price">$328</p></div>
  <div class="promo v-pink col-2 row-1"><div class="product-photo" role="img" aria-label="Stack of printed flyers"></div><div class="ribbon">Special</div><p class="detail">Full Color Front<br>100 lb Gloss + AQ</p><h2 class="title">Flyers</h2><p class="qty">5000<small>for</small></p><p class="price">$328</p></div>
  <div class="promo v-sky col-3 row-1"><div class="product-photo" role="img" aria-label="Stack of printed flyers"></div><div class="ribbon">Special</div><p class="detail">Full Color Front<br>100 lb Gloss + AQ</p><h2 class="title">Flyers</h2><p class="qty">5000<small>for</small></p><p class="price">$328</p></div>
  <div class="promo v-violet col-4 row-1"><div class="product-photo" role="img" aria-label="Stack of printed flyers"></div><div class="ribbon">Special</div><p class="detail">Full Color Front<br>100 lb Gloss + AQ</p><h2 class="title">Flyers</h2><p class="qty">5000<small>for</small></p><p class="price">$328</p></div>

  <!-- Postcards -->
  <div class="promo v-orange col-1 row-2"><div class="product-photo postcard" role="img" aria-label="Printed postcards"></div><div class="ribbon">Special</div><p class="detail">Full Color Front<br>14pt with UV Coating</p><h2 class="title">Postcards</h2><p class="qty">5000<small>for</small></p><p class="price">$237</p></div>
  <div class="promo v-pink col-2 row-2"><div class="product-photo postcard" role="img" aria-label="Printed postcards"></div><div class="ribbon">Special</div><p class="detail">Full Color Front<br>14pt with UV Coating</p><h2 class="title">Postcards</h2><p class="qty">5000<small>for</small></p><p class="price">$237</p></div>
  <div class="promo v-sky col-3 row-2"><div class="product-photo postcard" role="img" aria-label="Printed postcards"></div><div class="ribbon">Special</div><p class="detail">Full Color Front<br>14pt with UV Coating</p><h2 class="title">Postcards</h2><p class="qty">5000<small>for</small></p><p class="price">$237</p></div>
  <div class="promo v-violet col-4 row-2"><div class="product-photo postcard" role="img" aria-label="Printed postcards"></div><div class="ribbon">Special</div><p class="detail">Full Color Front<br>14pt with UV Coating</p><h2 class="title">Postcards</h2><p class="qty">5000<small>for</small></p><p class="price">$237</p></div>

  <!-- Brochures -->
  <div class="promo v-orange col-1 row-3"><div class="product-photo brochure" role="img" aria-label="Open tri-fold brochure"></div><div class="ribbon">Special</div><p class="detail brochure-detail">Full Color<br>8.5"x11" Tri-Fold</p><h2 class="title brochure-title">Brochures</h2><p class="qty">5000<small>for</small></p><p class="price">$386</p></div>
  <div class="promo v-pink col-2 row-3"><div class="product-photo brochure" role="img" aria-label="Open tri-fold brochure"></div><div class="ribbon">Special</div><p class="detail brochure-detail">Full Color<br>8.5"x11" Tri-Fold</p><h2 class="title brochure-title">Brochures</h2><p class="qty">5000<small>for</small></p><p class="price">$386</p></div>
  <div class="promo v-sky col-3 row-3"><div class="product-photo brochure" role="img" aria-label="Open tri-fold brochure"></div><div class="ribbon">Special</div><p class="detail brochure-detail">Full Color<br>8.5"x11" Tri-Fold</p><h2 class="title brochure-title">Brochures</h2><p class="qty">5000<small>for</small></p><p class="price">$386</p></div>
  <div class="promo v-violet col-4 row-3"><div class="product-photo brochure" role="img" aria-label="Open tri-fold brochure"></div><div class="ribbon">Special</div><p class="detail brochure-detail">Full Color<br>8.5"x11" Tri-Fold</p><h2 class="title brochure-title">Brochures</h2><p class="qty">5000<small>for</small></p><p class="price">$386</p></div>

  <!-- Table Tents -->
  <div class="promo v-orange col-1 row-4"><div class="product-photo tall" role="img" aria-label="Folded table tent card"></div><div class="ribbon">Special</div><p class="detail">Full Color Front<br>14pt with UV Coating</p><h2 class="title">Table Tents</h2><p class="qty">1000<small>for</small></p><p class="price">$217</p></div>
  <div class="promo v-pink col-2 row-4"><div class="product-photo tall" role="img" aria-label="Folded table tent card"></div><div class="ribbon">Special</div><p class="detail">Full Color Front<br>14pt with UV Coating</p><h2 class="title">Table Tents</h2><p class="qty">1000<small>for</small></p><p class="price">$217</p></div>
  <div class="promo v-sky col-3 row-4"><div class="product-photo tall" role="img" aria-label="Folded table tent card"></div><div class="ribbon">Special</div><p class="detail">Full Color Front<br>14pt with UV Coating</p><h2 class="title">Table Tents</h2><p class="qty">1000<small>for</small></p><p class="price">$217</p></div>
  <div class="promo v-violet col-4 row-4"><div class="product-photo tall" role="img" aria-label="Folded table tent card"></div><div class="ribbon">Special</div><p class="detail">Full Color Front<br>14pt with UV Coating</p><h2 class="title">Table Tents</h2><p class="qty">1000<small>for</small></p><p class="price">$217</p></div>
</main>
</body>
</html>
```